Business Card Design Project

I need a business card design for our new logo, please check the logo at the following link:
https://www.boxtrove.net/s/k7pqwe93mz41xr/TulipCrew.png
The address on the business card:
Av. Orlândio Vasconte 418 sala 207
Barra da Tijuca, Rio de Janeiro, RJ
CEP: 22719-480
Brasil
Phone: +55 21 74302186
e-mail: renato@tulipcrew.com.br
Updates
Thank you all for sending your designs, we will not provide feedback because there are too many designs, on December 3 we will pick the best design according to our point of view. Please keep posting.
Renato

```html
<!DOCTYPE html>
<html lang="pt-BR">
<head>
<meta charset="utf-8">
<title>TulipCrew – Business Card</title>
<link rel="stylesheet" href="https://fonts.googleapis.com/css2?family=PT+Sans:wght@400;700&display=swap">
<style>
  :root {
    --backdrop: #e9e6e1;
    --card-white: #ffffff;
    --brand-yellow: #f7c800;
    --ink: #2a2a2a;
    --ink-soft: #555555;
    --swoosh: #5a5a5a;
    --divider: #b5b5b5;
    --address-ink: #8a6a00;
  }
  * { margin: 0; padding: 0; box-sizing: border-box; }
  html, body {
    width: 1200px; height: 758px; overflow: hidden;
    background: var(--backdrop);
    font-family: "PT Sans", Arial, sans-serif;
  }
  .stage {
    position: relative; width: 1200px; height: 758px;
    display: flex; align-items: center; justify-content: center; gap: 50px;
  }
  .card {
    position: relative; width: 520px; height: 297px;
    box-shadow: 0 6px 18px rgba(0,0,0,.18);
    overflow: hidden;
  }
  .card--front { background: var(--card-white); }
  .card--back { background: var(--brand-yellow); display: flex; align-items: center; justify-content: center; }
  .card-band { position: absolute; inset: 0; width: 100%; height: 100%; }

  .brand {
    position: absolute; left: 60px; top: 100px;
    display: flex; align-items: center; gap: 10px;
  }
  .brand-mark { width: 20px; height: 20px; background: var(--brand-yellow); }
  .brand-name { font-size: 30px; font-weight: 700; color: var(--ink); }

  .divider {
    position: absolute; left: 250px; top: 62px; width: 2px; height: 112px;
    background: linear-gradient(var(--divider), rgba(181,181,181,0));
  }
  .contact { position: absolute; left: 272px; top: 66px; color: var(--ink-soft); }
  .contact-name { font-size: 19px; font-weight: 700; color: var(--ink); line-height: 1.1; }
  .contact-title { font-size: 14px; margin-bottom: 14px; }
  .contact-line { display: flex; align-items: center; gap: 6px; font-size: 13px; line-height: 1.6; }
  .contact-line svg { width: 11px; height: 11px; fill: var(--ink-soft); }

  .address {
    position: absolute; right: 34px; bottom: 24px; width: 380px;
    text-align: center; font-size: 13px; line-height: 1.45; color: var(--address-ink);
  }
  .back-brand { font-size: 54px; font-weight: 700; color: var(--ink); }
</style>
</head>
<body>
<main class="stage">
  <section class="card card--front" aria-label="Card front">
    <svg class="card-band" viewBox="0 0 520 297" aria-hidden="true">
      <path d="M0,190 Q300,225 520,92 L520,297 L0,297 Z" fill="var(--brand-yellow)"/>
      <path d="M30,185 Q300,214 500,88 Q320,203 30,185 Z" fill="var(--swoosh)"/>
    </svg>
    <div class="brand">
      <span class="brand-mark"></span>
      <span class="brand-name">TulipCrew</span>
    </div>
    <div class="divider"></div>
    <div class="contact">
      <p class="contact-name">Your Name</p>
      <p class="contact-title">Title</p>
      <p class="contact-line">
        <svg viewBox="0 0 24 24"><path d="M6.6 10.8a15 15 0 0 0 6.6 6.6l2.2-2.2a1 1 0 0 1 1-.25 11.4 11.4 0 0 0 3.6.57 1 1 0 0 1 1 1V20a1 1 0 0 1-1 1A17 17 0 0 1 3 4a1 1 0 0 1 1-1h3.5a1 1 0 0 1 1 1c0 1.25.2 2.45.57 3.57a1 1 0 0 1-.25 1z"/></svg>
        +55 21 74302186
      </p>
      <p class="contact-line">
        <svg viewBox="0 0 24 24"><path d="M2 6h20v12H2z M2 6l10 7 10-7" fill="none" stroke="var(--ink-soft)" stroke-width="2.4"/></svg>
        renato@tulipcrew.com.br
      </p>
    </div>
    <p class="address">Av. Orlândio Vasconte 418 sala 207<br>Barra da Tijuca, Rio de Janeiro, RJ, CEP: 22719-480, Brasil</p>
  </section>

  <section class="card card--back" aria-label="Card back">
    <span class="back-brand">TulipCrew</span>
  </section>
</main>
</body>
</html>
```